Brantley Water Taxi and Transport

Need to redesign our business cards to relay that we do freight logistics and water taxi service. We also work with gov. agencies doing environmental clean up, oil spill response, remote site construction and work with many of the air taxi and helicopter services on Kodiak Island. Out website is www.brantleywatertaxi-example.com to get a better idea of what we do.

Contact Information for Business Card

I have a previous business card but it just has the logo on the front, and a sunset picture on the back with the contact info. It does not relay what we do and what we can help with. I like a simple straight forward design over a busy one.

Colors
3176b5
0455a3
cfdfed

Requirements
Must have
• logo, email, website, phone number

```html
<!DOCTYPE html>
<html lang="en">
<head>
<meta charset="utf-8">
<title>Brantley Water Taxi and Transport – Business Cards</title>
<link href="https://fonts.googleapis.com/css2?family=Montserrat:wght@300;600&family=Open+Sans:wght@600;700&display=swap" rel="stylesheet">
<style>
  :root {
    --page-bg: #dcdde0;
    --brand-blue: #0455a3;
    --mid-blue: #3176b5;
    --pale-blue: #cfdfed;
    --sky-blue: #5bb4e2;
    --sun-orange: #f3a321;
    --ink: #233044;
    --white: #ffffff;
  }
  * { box-sizing: border-box; margin: 0; padding: 0; }
  html, body { width: 1200px; height: 1053px; overflow: hidden; }
  body {
    background: var(--page-bg);
    position: relative;
    font-family: "Open Sans", sans-serif;
  }
  .card {
    position: absolute;
    left: 323px;
    width: 553px;
    height: 316px;
    overflow: hidden;
  }
  .card-front { top: 170px; background: var(--white); }
  .card-back {
    top: 566px;
    background: radial-gradient(ellipse at 50% 40%, #2272b8 0%, #1559a6 60%, #11509d 100%);
  }

  .logo-art {
    position: absolute;
    left: 145px; top: 26px;
    width: 264px; height: 128px;
    border-radius: 4px;
    background: linear-gradient(180deg, #fdf3e2 0%, #d9ecf7 45%, #9fcde9 100%);
  }
  .brand-name {
    font-family: "Montserrat", sans-serif;
    font-weight: 600;
    text-align: center;
    letter-spacing: 0.5px;
  }
  .brand-tagline {
    font-family: "Montserrat", sans-serif;
    font-weight: 300;
    text-align: center;
  }
  .card-front .brand-name {
    position: absolute; left: 0; right: 0; top: 166px;
    font-size: 32px; line-height: 1; color: var(--brand-blue);
  }
  .card-front .brand-tagline {
    position: absolute; left: 0; right: 0; top: 202px;
    font-size: 14px; color: var(--ink);
  }

  .contact-band {
    position: absolute; left: 0; right: 0; top: 232px; height: 84px;
    background: radial-gradient(ellipse at 50% 80%, #2272b8 0%, #1559a6 70%);
  }
  .wave-strip {
    position: absolute; left: 0; right: 0; height: 12px;
    background: linear-gradient(90deg, rgba(207,223,237,0.15), rgba(207,223,237,0.6) 50%, rgba(207,223,237,0.15));
    border-radius: 6px;
  }
  .contact-band .wave-strip { top: 12px; }
  .contact-list {
    position: absolute; left: 0; right: 0; top: 46px;
    display: flex; justify-content: space-between; align-items: center;
    padding: 0 36px 0 48px;
    list-style: none;
  }
  .contact-item {
    display: flex; align-items: center; gap: 10px;
    color: var(--white); font-weight: 700; font-size: 10px;
  }
  .contact-item.email { font-size: 8.5px; }
  .contact-icon {
    width: 20px; height: 20px; border-radius: 50%;
    background: var(--white);
    display: flex; align-items: center; justify-content: center;
  }
  .contact-icon svg { width: 12px; height: 12px; }

  .card-back .brand-name {
    position: absolute; left: 0; right: 0; top: 100px;
    font-size: 50px; line-height: 1; color: var(--white);
  }
  .card-back .brand-tagline {
    position: absolute; left: 0; right: 0; top: 157px;
    font-size: 24px; color: var(--white);
  }
  .card-back .wave-strip { top: 242px; }
  .website {
    position: absolute; left: 0; right: 0; top: 280px;
    text-align: center; color: var(--white);
    font-size: 11px; font-weight: 700; letter-spacing: 3px;
  }
</style>
</head>
<body>
  <section class="card card-front">
    <div class="logo-art" role="img" aria-label="Illustration of a workboat on waves before blue mountains and an orange sun"></div>
    <h1 class="brand-name">BRANTLEY</h1>
    <p class="brand-tagline">Water Taxi &amp; Transport</p>
    <div class="contact-band">
      <div class="wave-strip" role="img" aria-label="Decorative wave line"></div>
      <ul class="contact-list">
        <li class="contact-item phone">
          <span class="contact-icon">
            <svg viewBox="0 0 24 24"><path fill="#0455a3" d="M6.6 10.8a15.1 15.1 0 0 0 6.6 6.6l2.2-2.2c.3-.3.7-.4 1-.2 1.1.4 2.3.6 3.6.6.6 0 1 .4 1 1V20c0 .6-.4 1-1 1A17 17 0 0 1 3 4c0-.6.4-1 1-1h3.5c.6 0 1 .4 1 1 0 1.3.2 2.5.6 3.6.1.3 0 .7-.2 1z"/></svg>
          </span>
          555 010 3400
        </li>
        <li class="contact-item email">
          <span class="contact-icon">
            <svg viewBox="0 0 24 24"><rect x="3" y="6" width="18" height="12" rx="1" fill="#0455a3"/><path d="M3.5 6.5 12 13l8.5-6.5" stroke="#fff" stroke-width="1.6" fill="none"/></svg>
          </span>
          brantleywatertaxi@example.com
        </li>
        <li class="contact-item social">
          <span class="contact-icon"></span>
          @brantleywatertaxi
        </li>
      </ul>
    </div>
  </section>

  <section class="card card-back">
    <h2 class="brand-name">BRANTLEY</h2>
    <p class="brand-tagline">Water Taxi &amp; Transport</p>
    <div class="wave-strip" role="img" aria-label="Decorative wave line"></div>
    <p class="website">www.brantleywatertaxi-example.com</p>
  </section>
</body>
</html>
```